Painting Contractor Business Card Design

We are looking for a cool, bold, modern, polished, business card design. We are a high-end residential painting contractor. Please incorporate our logo and keep with our green/black color scheme. We are interested in seeing 2-sided and 1-sided options. Thank you very much!

Industry/Entity Type

Business

Contact Information for Business Card

Info for the card:
Owen Talsky
mobile 206-555-0193
email owen@kestrowfinish.net
web www.kestrowfinish.net

```html
<!DOCTYPE html>
<html lang="en">
<head>
<meta charset="utf-8">
<title>Kestrow Finish – Business Card</title>
<link href="https://fonts.googleapis.com/css2?family=Lato:wght@400;700;900&display=swap" rel="stylesheet">
<style>
  :root {
    --backdrop: #121212;
    --card: #1b1b1c;
    --card-edge: #262627;
    --white: #f4f4f4;
    --text-soft: #d8d8d8;
    --green: #3fb54a;
    --spectrum: linear-gradient(180deg, #f6c21c 0%, #9ccf3a 30%, #37b9a0 50%, #f0b323 72%, #ef7a2a 100%);
  }
  * { box-sizing: border-box; margin: 0; padding: 0; }
  html, body { width: 1200px; height: 864px; overflow: hidden; }
  body {
    background: var(--backdrop);
    font-family: "Lato", Arial, sans-serif;
    display: flex;
    align-items: center;
    justify-content: center;
    gap: 60px;
  }
  .card {
    position: relative;
    width: 500px;
    height: 286px;
    background: var(--card);
    border: 1px solid var(--card-edge);
    border-radius: 18px;
    box-shadow: 0 18px 40px rgba(0,0,0,.6);
    overflow: hidden;
  }
  .edge-band {
    position: absolute;
    top: 24px;
    bottom: 24px;
    width: 9px;
    border-radius: 4px;
    background: var(--spectrum);
  }
  .edge-band--left { left: 14px; }
  .edge-band--right { right: 14px; }

  .contact-block { position: absolute; left: 48px; top: 56px; }
  .person-name {
    color: var(--white);
    font-weight: 900;
    font-size: 17px;
    letter-spacing: .3px;
    text-transform: uppercase;
  }
  .person-role {
    color: var(--green);
    font-size: 12px;
    letter-spacing: .5px;
    text-transform: uppercase;
    margin-top: 2px;
  }
  .contact-list { list-style: none; margin-top: 24px; }
  .contact-list li {
    display: flex;
    align-items: center;
    gap: 9px;
    color: var(--text-soft);
    font-size: 13px;
    line-height: 21px;
  }
  .contact-list svg { width: 12px; height: 12px; fill: var(--green); flex: none; }

  .divider {
    position: absolute;
    left: 262px;
    top: 62px;
    height: 160px;
    width: 1px;
    background: var(--green);
  }
  .front-brand {
    position: absolute;
    left: 263px;
    right: 23px;
    top: 0;
    bottom: 0;
    display: flex;
    align-items: center;
    justify-content: center;
    gap: 10px;
  }
  .brand-mark {
    width: 14px;
    height: 14px;
    background: var(--green);
    flex: none;
  }
  .brand-name {
    color: var(--white);
    font-weight: 900;
    text-transform: uppercase;
    letter-spacing: .5px;
  }
  .front-brand .brand-name { font-size: 22px; line-height: 1.1; }

  .back-brand {
    position: absolute;
    inset: 0 0 40px 0;
    display: flex;
    align-items: center;
    justify-content: center;
    gap: 12px;
  }
  .back-brand .brand-name { font-size: 30px; }
  .back-web {
    position: absolute;
    left: 0;
    right: 0;
    bottom: 52px;
    text-align: center;
    color: var(--green);
    font-size: 14px;
    letter-spacing: .3px;
  }
</style>
</head>
<body>
  <section class="card card--front" aria-label="Business card front">
    <span class="edge-band edge-band--left"></span>
    <span class="edge-band edge-band--right"></span>

    <div class="contact-block">
      <h1 class="person-name">Owen Talsky</h1>
      <p class="person-role">Manager</p>
      <ul class="contact-list">
        <li>
          <svg viewBox="0 0 24 24" aria-hidden="true"><path d="M6.6 10.8a15.1 15.1 0 0 0 6.6 6.6l2.2-2.2c.3-.3.7-.4 1-.2 1.1.4 2.3.6 3.6.6.6 0 1 .4 1 1V20c0 .6-.4 1-1 1A17 17 0 0 1 3 4c0-.6.4-1 1-1h3.5c.6 0 1 .4 1 1 0 1.3.2 2.5.6 3.6.1.3 0 .7-.2 1z"/></svg>
          206-555-0193
        </li>
        <li>
          <svg viewBox="0 0 24 24" aria-hidden="true"><path d="M2 5h20v14H2zm2 2v.5l8 5 8-5V7l-8 5z"/></svg>
          owen@kestrowfinish.net
        </li>
        <li>
          <svg viewBox="0 0 24 24" aria-hidden="true"><path d="M12 2a10 10 0 1 0 0 20 10 10 0 0 0 0-20zm6.9 6h-3a15 15 0 0 0-1.3-3.9A8 8 0 0 1 18.9 8zM12 4c.8 1.2 1.5 2.5 1.9 4h-3.8c.4-1.5 1.1-2.8 1.9-4zM4.3 14a8 8 0 0 1 0-4h3.4a16 16 0 0 0 0 4zm.8 2h3a15 15 0 0 0 1.3 3.9A8 8 0 0 1 5.1 16zm3-8h-3a8 8 0 0 1 4.3-3.9C8.8 5.3 8.4 6.6 8.1 8zM12 20c-.8-1.2-1.5-2.5-1.9-4h3.8c-.4 1.5-1.1 2.8-1.9 4zm2.3-6H9.7a14 14 0 0 1 0-4h4.6a14 14 0 0 1 0 4zm.3 5.9c.6-1.2 1-2.5 1.3-3.9h3a8 8 0 0 1-4.3 3.9zm1.7-5.9a16 16 0 0 0 0-4h3.4a8 8 0 0 1 0 4z"/></svg>
          www.kestrowfinish.net
        </li>
      </ul>
    </div>

    <span class="divider"></span>

    <div class="front-brand">
      <span class="brand-mark"></span>
      <span class="brand-name">Kestrow<br>Finish</span>
    </div>
  </section>

  <section class="card card--back" aria-label="Business card back">
    <div class="back-brand">
      <span class="brand-mark"></span>
      <span class="brand-name">Kestrow Finish</span>
    </div>
    <p class="back-web">www.kestrowfinish.net</p>
  </section>
</body>
</html>
```